Velmora Homecare - Website

MUST HAVE EXPERIENCE DESIGNING WEBSITES HEALTH CARE IN GENERAL AND/OR HOME NURSING SERVICES.

Details attached.

Number of Pages Required

1 page

Requirements
Must have
• Warm feel
caregivers

Color similar to the logo...

```html
<!DOCTYPE html>
<html lang="en">
<head>
<meta charset="utf-8">
<title>Velmora Homecare</title>
<link href="https://fonts.googleapis.com/css2?family=Poppins:wght@300;400;500;600;700&display=swap" rel="stylesheet">
<style>
:root{
  --teal:#13869f;
  --teal-soft:#5fb7b2;
  --orange:#f7931e;
  --orange-soft:#e9a254;
  --ink:#1f2a33;
  --text:#6b7178;
  --grey-band:#f4f4f4;
  --sky:#c4e9f7;
  --white:#ffffff;
  --line:#e3e3e3;
}
*{margin:0;padding:0;box-sizing:border-box}
html,body{width:1200px;height:3151px;overflow:hidden;background:var(--white)}
body{position:relative;font-family:'Poppins',sans-serif;color:var(--text)}
.abs{position:absolute}
a{text-decoration:none;color:inherit}

/* hero */
.hero{left:0;top:0;width:1200px;height:563px;overflow:hidden}
.hero-photo{position:absolute;inset:0;background:linear-gradient(110deg,#6cc0b8 0%,#8ec4b0 30%,#d9b882 60%,#eea45a 85%,#e99a48 100%)}
.hero-wave{position:absolute;left:0;top:0}
.brand{left:133px;top:0;width:173px;height:86px;background:var(--white);border-radius:0 0 4px 4px;display:flex;align-items:center;justify-content:center;gap:8px;box-shadow:0 2px 8px rgba(0,0,0,.06)}
.brand-dot{width:14px;height:14px;border-radius:50%;background:var(--teal)}
.brand-name{font-weight:600;font-size:14px;color:var(--teal);line-height:1.1}
.nav{top:40px;left:0;width:1200px;font-size:11px;color:var(--ink)}
.nav span{position:absolute;top:0;white-space:nowrap}
.nav .active{border-bottom:1px solid var(--ink)}
.btn{display:inline-flex;align-items:center;justify-content:center;border-radius:16px;font-weight:600;font-size:10px}
.btn-orange{background:var(--orange);color:var(--ink)}
.join{left:953px;top:37px;width:111px;height:24px}
.hero-title{left:200px;top:183px;width:460px;font-size:26px;line-height:31px;color:var(--white);font-weight:400}
.hero-contact{left:200px;top:309px;width:100px;height:30px}
.hero-more{left:313px;top:309px;width:75px;height:30px;border:1.5px solid var(--white);color:var(--white)}

/* specialize */
.spec-title{left:313px;top:634px;font-size:13px;color:var(--ink)}
.spec-title .t{color:var(--teal);font-weight:500}
.spec-title .o{color:var(--orange);font-weight:500}
.spec-text{left:313px;width:574px;font-size:11px;line-height:16.5px;text-align:justify}
.link{font-size:9.5px;color:var(--orange);display:flex;align-items:center;gap:5px}

/* services */
.services-band{left:0;top:871px;width:1200px;height:466px;background:var(--grey-band)}
.section-title{font-weight:700;font-size:22px;color:var(--teal);letter-spacing:.3px;white-space:nowrap}
.section-title .dash{color:var(--teal);font-weight:500;margin:0 8px}
.services-intro{left:134px;top:1027px;width:280px;font-size:11px;line-height:19px}
.card{background:var(--white);border-radius:6px;overflow:hidden;width:293px;height:302px;box-shadow:0 2px 10px rgba(0,0,0,.05)}
.card-photo{height:157px}
.card-body{padding:20px 18px}
.card-title{font-size:14.5px;font-weight:500;color:var(--orange);line-height:16px}
.card-text{margin-top:12px;font-size:10.5px;line-height:18px}
.card .link{margin-top:10px;font-size:9px}

/* testimonials */
.center{left:0;width:1200px;text-align:center}
.quote-badge{left:570px;top:1465px;width:60px;height:60px;border-radius:50%;background:#ededed;display:flex;align-items:center;justify-content:center}
.quote-text{left:254px;top:1543px;width:692px;text-align:center;font-size:11px;line-height:17.5px}
.quote-meta{top:1615px;left:0;width:1200px;display:flex;justify-content:center;align-items:center;gap:14px;font-size:9px;color:var(--teal)}
.quote-meta .name{font-weight:600;font-size:10.5px}
.quote-meta .sep{width:1px;height:14px;background:var(--line)}
.pager{top:1652px;left:0;width:1200px;display:flex;justify-content:center;align-items:center;gap:6px}
.pager i{width:7px;height:7px;border-radius:50%;border:1px solid #9aa;display:block}
.pager i.on{width:9px;height:9px;background:var(--teal);border-color:var(--teal)}

/* corona */
.covid-band{left:0;top:1731px;width:1200px;height:306px;background:var(--sky)}
.covid-art{left:232px;top:1786px;width:296px;height:177px;border-radius:50%;background:radial-gradient(circle at 50% 50%,#eaf6fb 0%,#d6eef8 55%,#9fd6c9 100%)}
.covid-title{left:602px;top:1810px}
.covid-sub{left:604px;top:1854px;font-size:17px;font-weight:600;color:var(--ink)}
.covid-text{left:604px;top:1883px;width:380px;font-size:11px;line-height:17.5px;color:var(--ink)}

/* news */
.news-card{left:193px;top:2171px;width:378px;height:312px;border-radius:8px;overflow:hidden;box-shadow:0 4px 14px rgba(0,0,0,.08)}
.news-photo{position:absolute;inset:0;background:linear-gradient(120deg,#d9d5cf 0%,#c9b39a 45%,#efe9e3 100%)}
.news-caption{position:absolute;left:0;top:196px;width:277px;height:116px;background:var(--white);padding:28px 30px}
.news-caption .meta{font-size:8px;color:var(--text)}
.news-caption .head{margin-top:10px;font-size:10.5px;line-height:16px;color:var(--ink)}
.press-label{left:630px;top:2187px;font-size:8.5px;letter-spacing:1.5px;font-weight:600;color:var(--orange)}
.press-item{left:630px;width:375px;border-top:1px solid var(--line);padding-top:12px}
.press-item p{font-size:10px;line-height:15px;color:var(--ink)}
.press-item .date{margin-top:6px;font-size:8.5px;color:var(--ink)}

/* quote footer */
.foot-wave{left:0;top:2545px}
.quote-title{font-size:24px;font-weight:600;color:var(--white)}
.quote-title .dash{font-weight:400;margin:0 8px}
.quote-sub{font-size:9px;color:var(--white)}
.field{height:30px;border-radius:15px;background:var(--white);font-size:9px;color:#a8adb2;padding:10px 16px}
.field.msg{height:73px;border-radius:12px}
.request{left:531px;top:3008px;width:137px;height:30px;font-size:10px}
.social{left:1022px;width:30px;height:30px;border-radius:50%;border:1px solid rgba(255,255,255,.6);background:rgba(255,255,255,.12)}
.copy{left:134px;top:3085px;font-size:9.5px;color:var(--ink)}
.call{top:3073px;font-size:19px;color:var(--ink)}
.mail{top:3103px;font-size:9px;color:var(--ink)}
.foot-links{left:839px;top:3085px;font-size:9.5px;color:var(--ink);white-space:nowrap}
</style>
</head>
<body>

<!-- hero -->
<section class="hero abs">
  <div class="hero-photo" role="img" aria-label="Caregiver smiling with an elderly woman at home, in soft teal and orange tones"></div>
  <svg class="hero-wave" width="1200" height="563" viewBox="0 0 1200 563">
    <path d="M0 378 C120 360 230 420 330 500 C420 570 540 575 640 510 C760 430 850 370 960 378 C1060 385 1140 440 1200 502 L1200 563 L0 563 Z" fill="#ffffff"/>
  </svg>
</section>

<div class="brand abs"><span class="brand-dot"></span><span class="brand-name">Velmora<br>Homecare</span></div>

<nav class="nav abs">
  <span class="active" style="left:421px">Home</span>
  <span style="left:470px">About Us</span>
  <span style="left:535px">Services</span>
  <span style="left:597px">Testimonials</span>
  <span style="left:681px">News</span>
  <span style="left:729px">Contact Us</span>
  <span style="left:817px;font-size:10px">Call.
    <svg width="9" height="9" viewBox="0 0 24 24" style="vertical-align:-1px;margin:0 2px"><path d="M6.6 10.8a15 15 0 0 0 6.6 6.6l2.2-2.2c.3-.3.7-.4 1-.2 1.1.4 2.3.6 3.6.6.6 0 1 .4 1 1V20c0 .6-.4 1-1 1A17 17 0 0 1 3 4c0-.6.4-1 1-1h3.5c.6 0 1 .4 1 1 0 1.3.2 2.5.6 3.6.1.3 0 .7-.2 1z" fill="#1f2a33"/></svg>+1 800 555 01 23</span>
</nav>
<a class="btn btn-orange join abs">Join our Team</a>

<h1 class="hero-title abs">Lorem ipsum dolor sit amet, consectetur adipiscing elit, sed do eiusmod tempor.</h1>
<a class="btn btn-orange hero-contact abs">Contact Us</a>
<a class="btn hero-more abs">More</a>

<!-- specialize -->
<h2 class="spec-title abs"><span class="t">Velmora</span> <span class="o">Homecare</span> Specialize</h2>
<p class="spec-text abs" style="top:669px">Everyone should be free to experience joy and optimism in their lives, regardless of their age or condition. Velmora Homecare provides a range of services that are tailored to meet the patient's needs, helping them to maintain their independence and live happy and fulfilling lives.</p>
<p class="spec-text abs" style="top:734px">Velmora Homecare deliver comprehensive care to new porn baby and mother, and elderly in the comfort of their own homes, we ensure that the needs of our clients and their families are at the heart of everything they do.</p>
<a class="link abs" style="left:313px;top:807px">Our Company <span>&rarr;</span></a>

<!-- services -->
<section class="services-band abs"></section>
<h2 class="section-title abs" style="left:134px;top:980px">SERVICES<span class="dash">--</span></h2>
<p class="services-intro abs">Lorem Ipsum is simply dummy text of the printing and typesetting industry. Lorem Ipsum has been the industry's standard dummy text...</p>

<article class="card abs" style="left:460px;top:953px">
  <div class="card-photo" role="img" aria-label="Smiling nurse holding a clipboard in a clinic" style="background:linear-gradient(120deg,#2f8fa6 0%,#9ec7cf 50%,#e7ecec 100%)"></div>
  <div class="card-body">
    <h3 class="card-title">Home Nursing Services</h3>
    <p class="card-text">Looking for care, custodial care, Urinary catheterization care, Wound care, Injections, IV infusions, Vaccination or other nursing...</p>
    <a class="link">Read More <span>&rarr;</span></a>
  </div>
</article>
<article class="card abs" style="left:772px;top:953px">
  <div class="card-photo" role="img" aria-label="Mother holding her newborn baby close" style="background:linear-gradient(120deg,#f3ede6 0%,#e8c7a4 55%,#f6efe8 100%)"></div>
  <div class="card-body">
    <h3 class="card-title">New Born Baby And Mother Care At Home</h3>
    <p class="card-text">Worried about your newborn's needs? Facing issues in coping up with the initial...</p>
    <a class="link">Read More <span>&rarr;</span></a>
  </div>
</article>

<!-- testimonials -->
<h2 class="section-title abs center" style="top:1407px"><span class="dash">--</span>TESTIMONIALS<span class="dash">--</span></h2>
<div class="quote-badge abs">
  <svg width="26" height="20" viewBox="0 0 26 20"><path d="M0 20V11C0 5 3 1 9 0l1 3C7 4 5.5 6 5.5 9H10v11zM15 20V11c0-6 3-10 9-11l1 3c-3 1-4.5 3-4.5 6H25v11z" fill="#f7931e"/></svg>
</div>
<p class="quote-text abs">Lorem Ipsum is simply dummy text of the printing and typesetting industry. Lorem Ipsum has been the industry's standard dummy text ever since the 1500s, when an unknown printer took a galley of type and scrambled it to make a type specimen book. It has survived not only five centuries, but also the leap...</p>
<div class="quote-meta abs">
  <span><svg width="11" height="11" viewBox="0 0 24 24" style="vertical-align:-2px;margin-right:5px"><rect x="3" y="5" width="18" height="16" rx="2" fill="none" stroke="#13869f" stroke-width="2"/><path d="M3 10h18M8 3v4M16 3v4" stroke="#13869f" stroke-width="2"/></svg>30 Nov, 2020</span>
  <span class="sep"></span>
  <span class="name">Marco Delgado</span>
</div>
<div class="pager abs"><i></i><i class="on"></i><i></i><a class="link" style="margin-left:8px;font-size:9px">View All <span>&rarr;</span></a></div>

<!-- corona -->
<section class="covid-band abs"></section>
<div class="covid-art abs" role="img" aria-label="Illustrated family in face masks behind a shield, surrounded by virus particles"></div>
<h2 class="section-title abs covid-title">CORONAVIRUS UPDATE<span class="dash">--</span></h2>
<h3 class="covid-sub abs">Protect Your Family From Covid</h3>
<p class="covid-text abs">Lorem Ipsum is simply dummy text of the printing and typesetting industry. Lorem Ipsum has been the industry's</p>
<a class="link abs" style="left:604px;top:1940px">Read more <span>&rarr;</span></a>

<!-- news -->
<h2 class="section-title abs center" style="top:2100px"><span class="dash">--</span>NEWS<span class="dash">--</span></h2>
<article class="news-card abs">
  <div class="news-photo" role="img" aria-label="Adult daughter and her elderly mother laughing together"></div>
  <div class="news-caption">
    <p class="meta">Apr 2 2021 &nbsp;I&nbsp; By Admin</p>
    <p class="head">7 Ways to Bring Hope and Spread Kindness this National Month of Hope</p>
  </div>
</article>
<p class="press-label abs">PRESS RELEASE</p>
<div class="press-item abs" style="top:2215px"><p>Lorem ipsum dolor sit amet, consectetur adipiscing elit, sed do eiusmod tempor incididunt ut labore et dolore magna aliqua</p><p class="date">JUN 26 2021</p></div>
<div class="press-item abs" style="top:2290px"><p>Lorem ipsum dolor sit amet, consectetur adipiscing elit, sed do eiusmod tempor incididunt ut labore et dolore magna aliqua</p><p class="date">JUN 26 2021</p></div>
<div class="press-item abs" style="top:2365px"><p>Lorem ipsum dolor sit amet, consectetur adipiscing elit, sed do eiusmod tempor incididunt ut labore et dolore magna aliqua</p><p class="date">JUN 26 2021</p></div>
<div class="abs" style="left:630px;top:2440px;width:375px;border-top:1px solid var(--line)"></div>
<a class="link abs" style="left:630px;top:2456px">Explore All <span>&rarr;</span></a>

<!-- quick quote footer -->
<svg class="foot-wave abs" width="1200" height="606" viewBox="0 0 1200 606">
  <defs>
    <linearGradient id="footGrad" x1="0" y1="1" x2="1" y2="0">
      <stop offset="0" stop-color="#5fb0a6"/>
      <stop offset="0.5" stop-color="#a7a866"/>
      <stop offset="1" stop-color="#eb9a3c"/>
    </linearGradient>
  </defs>
  <path d="M0 30 C100 40 220 110 360 95 C520 78 600 20 760 5 C920 -8 1060 30 1200 70 L1200 606 L0 606 Z" fill="url(#footGrad)"/>
  <path d="M1200 140 C1080 150 920 220 915 320 C910 430 1050 470 1120 520 C1160 550 1190 580 1200 606 Z" fill="#e7973a" opacity=".55"/>
</svg>

<h2 class="quote-title abs center" style="top:2730px"><span class="dash">--</span>Get A Quick Quote<span class="dash">--</span></h2>
<p class="quote-sub abs center" style="top:2767px">Duis aute irure dolor in reprehenderit in voluptate velit esse cillum dolore eu fugiat nulla.</p>
<div class="field abs" style="left:313px;top:2808px;width:277px">Enter your Name</div>
<div class="field abs" style="left:609px;top:2808px;width:278px">Email</div>
<div class="field abs" style="left:313px;top:2859px;width:277px">Phone</div>
<div class="field abs" style="left:609px;top:2859px;width:278px">Subject</div>
<div class="field msg abs" style="left:313px;top:2909px;width:574px">Message ...</div>
<a class="btn btn-orange request abs">Request A Quote</a>

<span class="social abs" style="top:2737px"></span>
<span class="social abs" style="top:2779px"></span>
<span class="social abs" style="top:2820px"></span>
<span class="social abs" style="top:2862px"></span>

<p class="copy abs">&copy; 2021 by Velmora Homecare</p>
<p class="call abs center">Call. <b style="font-weight:500">+1 800 555 0123</b></p>
<p class="mail abs center">E. info@velmora-homecare.com</p>
<p class="foot-links abs">Home &nbsp;I&nbsp; Company &nbsp;I&nbsp; Contact &nbsp;I&nbsp; Join our Team</p>

</body>
</html>
```